KMT Compliant Dietary Supplement Label for Nutritional Company

We are in need of a label for our line of 20+ dietary supplements that are specifically formulated to balance body chemistry and match the biochemical individuality of our users based on hair tissue mineral analysis.

We have a line of approximately 20 different dietary supplements that will require use of new label in both a small (90 capsule) and large (180 capsule) size. We will start with the initial label in which Product name, Supplement Facts, and Ingredient list will need to be modified for each particular product thereafter.

The label will be placed on a transparent blue bottle with the color of lid being decided after label design. We are open to a transparent light amber bottle with black lid but blue is our preference.

We would like the majority of the label to be blue. Solid blue, fading of blue to darker blue/black, or subtle background designs are welcome with involvement of white and hints of orange. We do not want pictorial images on the label.

Label size:
Small bottle (120cc): Label size ~ 2.25” x 5.875”
Large bottle (200cc): Label size ~ 2.75” x 7.625”

Front:
-Logo near top of label with product name and description in middle and capsule count near the bottom

Right Side:
-Supplement Facts: See current product image below in brief
-Ingredient list: See current product image below in brief
-Manufactured for: See image below (This is on the left side of our current bottle and would like it moved to the bottom of the right side)

Left side:
-Suggested use: See current product image below in brief
-Leave room for possible warning statement
-Leave room for possible lot number printing
-Keep out of the reach of children.

The first files below are our current supplement label with product information. This information is what is needed on the label and will likely need some adjustments as we are updating our line of supplements and changes in KMT requirements.

The following files are the logo files and color palette.

The remaining files are some designs we came across for inspiration.

Thank you.

Target Market(s)

Health Care Profressionals

Industry/Entity Type

Health Care and Nutrition

Requirements
Nice to have
• Product name needs to be on same line in all one color
Should not have
• Pictorial Images

```html
<!DOCTYPE html>
<html lang="en">
<head>
<meta charset="UTF-8">
<title>Orva-Tren Adrenal Supplement Label</title>
<link href="https://fonts.googleapis.com/css2?family=Montserrat:wght@400;500;700;800&display=swap" rel="stylesheet">
<style>
  :root {
    --page-bg: #f4f4f4;
    --label-white: #ffffff;
    --brand-blue: #2f5ba3;
    --panel-blue-dark: #2c5597;
    --panel-blue-light: #7596cf;
    --accent-orange: #f28a45;
    --accent-orange-light: #f6a062;
    --ink-dark: #1f2a44;
    --text-white: #ffffff;
  }
  * { margin: 0; padding: 0; box-sizing: border-box; }
  html, body {
    width: 1200px;
    height: 960px;
    overflow: hidden;
    background: var(--page-bg);
    font-family: "Montserrat", sans-serif;
  }
  .label {
    position: absolute;
    left: 397px;
    top: 316px;
    width: 396px;
    height: 502px;
    background: var(--label-white);
    overflow: hidden;
  }
  .brand {
    position: absolute;
    top: 84px;
    left: 0;
    width: 100%;
    text-align: center;
    color: var(--brand-blue);
    font-weight: 500;
  }
  .brand-mark {
    display: inline-block;
    width: 14px;
    height: 14px;
    border-radius: 50%;
    background: var(--accent-orange);
    vertical-align: middle;
    margin-right: 10px;
    position: relative;
    top: -4px;
  }
  .brand-name {
    font-size: 37px;
    letter-spacing: 1px;
    line-height: 1;
    vertical-align: middle;
  }
  .brand-sub {
    display: block;
    margin-top: 12px;
    font-size: 13px;
    letter-spacing: 8px;
    padding-left: 8px;
  }
  .product-panel {
    position: absolute;
    left: 26px;
    top: 192px;
    width: 338px;
    height: 320px;
    border-radius: 22px 22px 0 0;
    background: linear-gradient(200deg, var(--panel-blue-dark) 0%, #4d72b4 55%, var(--panel-blue-light) 100%);
  }
  .product-name {
    position: absolute;
    left: 0;
    width: 100%;
    text-align: center;
    color: var(--text-white);
    font-weight: 400;
    font-size: 98px;
    line-height: 1;
    letter-spacing: 2px;
  }
  .product-name--top { top: 17px; }
  .product-name--bottom { top: 116px; }
  .product-dash {
    position: absolute;
    left: 153px;
    top: 103px;
    width: 42px;
    height: 8px;
    background: var(--accent-orange);
  }
  .product-desc {
    position: absolute;
    left: 30px;
    top: 207px;
    width: 280px;
    height: 24px;
    background: linear-gradient(90deg, var(--accent-orange) 0%, var(--accent-orange-light) 100%);
    color: var(--text-white);
    font-weight: 700;
    font-size: 19px;
    line-height: 24px;
    text-align: center;
    letter-spacing: 0.3px;
  }
  .capsule-count {
    position: absolute;
    left: 0;
    top: 252px;
    width: 100%;
    text-align: center;
    white-space: nowrap;
  }
  .capsule-number {
    color: var(--accent-orange);
    font-weight: 800;
    font-size: 54px;
    line-height: 1;
    vertical-align: middle;
    letter-spacing: -2px;
  }
  .capsule-word {
    color: var(--text-white);
    font-weight: 700;
    font-size: 20px;
    vertical-align: middle;
    margin-left: 8px;
    position: relative;
    top: 4px;
  }
</style>
</head>
<body>
  <main class="label">
    <header class="brand">
      <span class="brand-mark"></span><span class="brand-name">VANTREL</span>
      <span class="brand-sub">LABORATORIES</span>
    </header>
    <section class="product-panel">
      <h1 class="product-name product-name--top">ORVA</h1>
      <span class="product-dash"></span>
      <h1 class="product-name product-name--bottom">TREN</h1>
      <p class="product-desc">ADRENAL SUPPLEMENT</p>
      <p class="capsule-count"><span class="capsule-number">90</span><span class="capsule-word">CAPSULES</span></p>
    </section>
  </main>
</body>
</html>
```